We are looking for a new website design for our SEO WEB Development Company. The URL is www.brellowcreativeworks.com

We want it to be a more powerful representation of what we do. We are also looking for a number of designers that we will give continuous business to every month. The persons design we choose will also get a proposal to complete 4 - 6 new designs for us every month for our clients.

Be creative as you can in your design submissions. We really want to stand out!

Just to give you an idea of what we like look at this site: http://www.tovandigitalstudio.com/

```html
<!DOCTYPE html>
<html lang="en">
<head>
<meta charset="utf-8">
<title>Brellow Interactive Group</title>
<link href="https://fonts.googleapis.com/css2?family=Noto+Serif&family=Arimo:wght@400&display=swap" rel="stylesheet">
<style>
:root{
  --brown:#a4520d;
  --orange:#c8690f;
  --orange-dark:#8e4507;
  --ink:#222;
  --muted:#555;
  --panel:#f1f1f1;
  --line:#d6d6d6;
  --foot-top:#4a4a4a;
  --foot-bot:#2b2b2b;
  --white:#fff;
}
*{margin:0;padding:0;box-sizing:border-box}
html,body{width:1200px;height:1082px;overflow:hidden;background:var(--white)}
body{font-family:"Arimo",Arial,sans-serif;color:var(--ink);position:relative}
.serif{font-family:"Noto Serif",Georgia,serif}
.abs{position:absolute}

.header{left:0;top:0;width:1200px;height:114px;background:linear-gradient(#fff,#e9e9e9)}
.brand{left:143px;top:14px;color:var(--brown);font-family:"Noto Serif",Georgia,serif;line-height:1}
.brand-name{font-size:64px;display:block}
.brand-sub{font-size:20px;display:block;margin-top:6px;letter-spacing:.5px}
.call{right:142px;top:42px;font-family:"Noto Serif",Georgia,serif;font-size:14px;color:var(--ink)}
.call b{font-family:"Arimo",sans-serif;font-weight:400;font-size:26px;color:var(--orange);letter-spacing:1px;margin-left:3px}
.nav{right:142px;top:88px;display:flex;font-family:"Noto Serif",Georgia,serif;font-size:16px}
.nav a{color:var(--ink);text-decoration:none;padding:0 9px;border-left:1px solid var(--orange)}
.nav a:first-child{border-left:0;color:var(--orange);font-size:17px}
.nav a:last-child{padding-right:0}

.band{left:0;top:114px;width:1200px;height:293px;background:linear-gradient(var(--orange-dark),var(--orange))}
.slider{left:135px;top:150px;width:930px;height:320px;background:var(--white);border-radius:5px;box-shadow:0 1px 4px rgba(0,0,0,.3)}
.hero{left:144px;top:158px;width:913px;height:304px;background:linear-gradient(100deg,#6d4a33 0%,#c9b8a3 35%,#ece6dd 55%,#b59b7c 80%,#8a7058 100%)}
.caption{left:144px;top:354px;width:312px;height:108px;background:linear-gradient(var(--orange),var(--orange-dark));color:var(--white);padding:8px 10px}
.caption h2{font-family:"Noto Serif",Georgia,serif;font-weight:400;font-size:30px}
.caption p{font-family:"Noto Serif",Georgia,serif;font-size:15px;line-height:18px;margin-top:8px;text-shadow:0 1px 1px rgba(0,0,0,.4)}
.tab{top:423px;width:199px;height:39px;background:linear-gradient(#fff,#dcdcdc);font-family:"Noto Serif",Georgia,serif;font-size:15px;display:flex;align-items:center;justify-content:center;color:var(--ink)}

.content{left:135px;top:478px;width:930px;height:367px;border:1px solid var(--line);border-radius:5px;background:var(--white)}
.services{left:142px;top:489px;width:656px;height:342px;background:linear-gradient(#fff,var(--panel));border:1px solid #e2e2e2;border-radius:4px}
.svc{top:502px;width:185px;text-align:center}
.svc h3{font-family:"Noto Serif",Georgia,serif;font-weight:400;font-size:17px;line-height:22px;color:var(--brown);height:52px}
.thumb{width:168px;height:104px;border:1px solid #ccc;padding:2px;background:var(--white);margin:0 auto}
.thumb div{width:100%;height:100%}
.svc p{font-size:11.5px;line-height:13.7px;text-align:left;margin:20px 0 0 10px;width:170px;color:var(--ink)}
.sep{top:502px;height:306px;border-left:1px dotted #bbb}
.more{top:795px;width:78px;height:24px;border-radius:3px;background:linear-gradient(var(--orange),var(--orange-dark));color:var(--white);font-size:11.5px;display:flex;align-items:center;justify-content:center}
.arrow{top:643px}

.quote{left:809px;top:489px;width:244px;height:342px;background:linear-gradient(#fff,var(--panel));border:1px solid #e2e2e2}
.quote-head{left:809px;top:489px;width:244px;height:33px;background:linear-gradient(var(--orange),var(--orange-dark));color:var(--white);font-family:"Noto Serif",Georgia,serif;font-size:17px;display:flex;align-items:center;justify-content:center}
.label{left:824px;font-size:11.5px;color:var(--ink)}
.field{left:822px;width:216px;height:26px;border:1px solid #ccc;border-radius:4px;background:var(--white)}
.btn{top:792px;width:86px;height:27px;border-radius:3px;display:flex;align-items:center;justify-content:center;font-size:13.5px}
.btn.submit{left:840px;background:linear-gradient(#555,#2a2a2a);color:var(--white)}
.btn.clear{left:935px;background:linear-gradient(#fff,#cfcfcf);border:1px solid #bbb;color:var(--ink)}

.footer{left:0;top:857px;width:1200px;height:225px;background:linear-gradient(var(--foot-top),var(--foot-bot));border-top:2px solid #333}
.fcol{top:874px;color:#ddd}
.fcol h4{font-family:"Noto Serif",Georgia,serif;font-weight:400;font-size:17.5px;color:#e6e6e6;margin-bottom:9px}
.fcol ul{list-style:none}
.fcol li{font-size:11.5px;line-height:16px;margin-bottom:1px;padding-left:10px;position:relative}
.fcol li::before{content:"»";position:absolute;left:0;color:#ccc}
.fcol li span{display:inline-block;border-bottom:1px solid #888;min-width:112px;padding:0 1px}
.copy{left:135px;top:1029px;width:932px;height:35px;border-radius:4px;background:linear-gradient(var(--orange),var(--orange-dark));color:var(--white);font-size:11.5px;display:flex;align-items:center;justify-content:center}
</style>
</head>
<body>

<header class="abs header"></header>
<div class="abs brand"><span class="brand-name">Brellow</span><span class="brand-sub">INTERACTIVE GROUP</span></div>
<div class="abs call">Call Now: <b>111-555-0142</b></div>
<nav class="abs nav"><a href="#">Home</a><a href="#">About Us</a><a href="#">Our Work</a><a href="#">Contact Us</a></nav>

<div class="abs band"></div>
<div class="abs slider"></div>
<div class="abs hero" role="img" aria-label="Photo of a team of business professionals reviewing documents"></div>
<div class="abs caption">
  <h2>Creative Design</h2>
  <p>Focusing on your Brand With the right Internet Marketing Tools</p>
</div>
<div class="abs tab" style="left:457px">Website Design</div>
<div class="abs tab" style="left:658px">Internet Marketing</div>
<div class="abs tab" style="left:859px">IT Consulting</div>

<div class="abs content"></div>
<div class="abs services"></div>

<section class="abs svc" style="left:163px">
  <h3>Brellow Interactive<br>Group</h3>
  <div class="thumb"><div role="img" aria-label="Photo of a group working together at a table" style="background:linear-gradient(135deg,#c9b59a,#e9e2d6 50%,#8d7a66)"></div></div>
  <p>is a leading Dallas Web Site Design, Publishing and Internet Marketing Firm. Our Dallas Texas based Website Design and Internet Marketing experts are some of the best in the industry!</p>
</section>
<div class="abs sep" style="left:370px"></div>
<section class="abs svc" style="left:366px">
  <h3>Brellow Interactive<br>Web</h3>
  <div class="thumb"><div role="img" aria-label="Image of a network cable against a digital globe" style="background:radial-gradient(circle at 40% 45%,#3d8fc9,#0e2c52 75%)"></div></div>
  <p>is a full-service Dallas based Advertising Agency comprised of experienced advertising and marketing professionals that provide clients with a clear and distinct voice in the market-place.</p>
</section>
<div class="abs sep" style="left:569px"></div>
<section class="abs svc" style="left:567px">
  <h3>Brellow Interactive<br>Publishing</h3>
  <div class="thumb"><div role="img" aria-label="Photo of a newspaper stack beside a keyboard" style="background:linear-gradient(160deg,#9aa7b8,#e6e8ec 55%,#b9bcc2)"></div></div>
  <p>provides full-service custom publishing and consulting services for magazines, news-letters, blogs and web sites. We are the complete interactive publishing arm for your organi-zation.</p>
</section>

<svg class="abs arrow" style="left:146px" width="32" height="32" viewBox="0 0 32 32" aria-hidden="true">
  <circle cx="16" cy="16" r="15" fill="#a86a2c" stroke="#7a4410" stroke-width="1"/>
  <path d="M18.5 9 L12 16 L18.5 23" fill="none" stroke="#fff" stroke-width="3" stroke-linecap="round"/>
</svg>
<svg class="abs arrow" style="left:759px" width="32" height="32" viewBox="0 0 32 32" aria-hidden="true">
  <circle cx="16" cy="16" r="15" fill="#8e4507" stroke="#6a3305" stroke-width="1"/>
  <path d="M13.5 9 L20 16 L13.5 23" fill="none" stroke="#fff" stroke-width="3" stroke-linecap="round"/>
</svg>

<div class="abs more" style="left:258px">Read More</div>
<div class="abs more" style="left:476px">Read More</div>
<div class="abs more" style="left:686px">Read More</div>

<aside class="abs quote"></aside>
<div class="abs quote-head">Get a Free Quote</div>
<div class="abs label" style="top:541px">Name</div>
<div class="abs field" style="top:556px"></div>
<div class="abs label" style="top:602px">Phone number</div>
<div class="abs field" style="top:617px"></div>
<div class="abs label" style="top:666px">Email</div>
<div class="abs field" style="top:681px"></div>
<div class="abs label" style="top:732px">Website Address</div>
<div class="abs field" style="top:747px"></div>
<div class="abs btn submit">Submit</div>
<div class="abs btn clear">Clear</div>

<footer class="abs footer"></footer>
<div class="abs fcol" style="left:180px">
  <h4>Creative Design</h4>
  <ul><li><span>Creative Advertising</span></li><li><span>Print Design</span></li><li><span>Corporate Identity</span></li><li><span>Packaging</span></li></ul>
</div>
<div class="abs fcol" style="left:350px">
  <h4>Internet Marketing Services</h4>
  <ul><li><span style="min-width:188px">Search Engine Optimization</span></li><li><span style="min-width:188px">Pay-per-Click Campaign Consulting</span></li><li><span style="min-width:188px">Email Marketing</span></li><li><span style="min-width:188px">SEO Copywriting</span></li><li><span style="min-width:188px">Reputation Management</span></li></ul>
</div>
<div class="abs fcol" style="left:623px">
  <h4>Website Design</h4>
  <ul><li><span style="min-width:80px">Web Design</span></li><li><span style="min-width:80px">E-commerce</span></li><li><span style="min-width:80px">Multimedia</span></li><li><span>Web Application Development</span></li></ul>
</div>
<div class="abs fcol" style="left:860px">
  <h4>IT Consulting</h4>
  <ul><li><span style="min-width:88px">Home</span></li><li><span style="min-width:88px">Our Work</span></li><li><span style="min-width:88px">About Us</span></li><li><span style="min-width:88px">contact Us</span></li></ul>
</div>
<div class="abs copy">Copyright © 2011 Brellowinteractivegroup.</div>

</body>
</html>
```